Real estate company needs a card that makes you say WOW!

We need an awesome business card for our real estate company, Stonebrook Realty Partners of Chicago, that will stand out from the crowd. We specialize in buying and selling real estate, property management, and real estate investments (Flips & Rentals). On the business card, I need the following:

- Our logo
- Services
- My name & contact info (Derek Ollanby, 630-517-2946, Derek@StonebrookRPC.com)
- My title (Director of Acquisitions)
- StonebrookRPC.com

I attached an EPS file of our logo. Let me know if you have any questions. Thank you in advance!

```html
<!DOCTYPE html>
<html lang="en">
<head>
<meta charset="utf-8">
<title>Stonebrook Realty Partners of Chicago – Business Card</title>
<link rel="stylesheet" href="https://fonts.googleapis.com/css2?family=Crimson+Pro:wght@400;600&display=swap">
<style>
  :root {
    --bg: #e9e9eb;
    --brand-blue: #145a9c;
    --brand-blue-deep: #0e5694;
    --brand-blue-mid: #1670b8;
    --sky-light: #29a3e0;
    --ink: #2a2a2a;
    --white: #ffffff;
  }
  * { box-sizing: border-box; margin: 0; padding: 0; }
  html, body { width: 1200px; height: 1000px; overflow: hidden; }
  body {
    position: relative;
    background: var(--bg);
    font-family: "Crimson Pro", Georgia, serif;
  }

  .card { position: absolute; }

  /* Back of card */
  .card-back {
    left: 284px; top: 492px; width: 852px; height: 482px;
    background: radial-gradient(ellipse at 50% 45%, var(--brand-blue-mid) 0%, var(--brand-blue-deep) 75%);
    box-shadow: 0 6px 14px rgba(0,0,0,.35);
    color: var(--white);
    text-align: center;
  }
  .back-brand {
    position: absolute; left: 0; right: 0; top: 198px;
    text-transform: uppercase; font-weight: 400; line-height: 1;
  }
  .back-brand .brand-main { display: block; font-size: 58px; letter-spacing: 2px; }
  .back-brand .brand-sub { display: block; font-size: 27px; letter-spacing: 1px; margin-top: 8px; }
  .services {
    position: absolute; left: 0; right: 0; top: 394px;
    list-style: none; font-size: 25px; line-height: 41px;
  }
  .services li { display: inline; margin: 0 8px; }
  .services .row { display: block; }

  /* Front of card */
  .card-front {
    left: 40px; top: 47px; width: 850px; height: 498px;
    background: var(--white);
    box-shadow: 0 6px 14px rgba(0,0,0,.35);
    overflow: hidden;
  }
  .front-brand {
    position: absolute; left: 35px; top: 52px;
    color: var(--brand-blue); text-transform: uppercase; font-weight: 400; line-height: 1;
  }
  .front-brand .brand-main { display: block; font-size: 54px; letter-spacing: 1px; }
  .front-brand .brand-sub { display: block; font-size: 24px; letter-spacing: .5px; margin-top: 4px; }

  .person { position: absolute; left: 40px; top: 200px; }
  .person-name { font-size: 27px; font-weight: 600; color: var(--brand-blue); line-height: 34px; }
  .person-title { font-size: 22px; color: var(--ink); line-height: 30px; }

  .contact { position: absolute; left: 40px; top: 326px; list-style: none; }
  .contact li {
    display: flex; align-items: center; height: 41px;
    font-size: 23px; color: var(--ink);
  }
  .contact svg { width: 20px; height: 20px; margin-right: 26px; fill: var(--brand-blue); }

  .skyline-art {
    position: absolute; left: 450px; top: 285px; width: 385px; height: 170px;
    background: linear-gradient(180deg, var(--sky-light) 0%, var(--brand-blue) 100%);
    opacity: .85;
  }
  .front-band {
    position: absolute; left: 0; right: 0; bottom: 0; height: 43px;
    background: linear-gradient(180deg, var(--brand-blue-mid), var(--brand-blue-deep));
  }
</style>
</head>
<body>

  <section class="card card-back" aria-label="Card back">
    <div class="back-brand">
      <span class="brand-main">Stonebrook</span>
      <span class="brand-sub">Realty Partners of Chicago</span>
    </div>
    <ul class="services">
      <span class="row"><li>• Real Estate Investments (Flips &amp; Rentals)</li></span>
      <span class="row"><li>• Property Management</li><li>• Buying and Selling Real Estate</li></span>
    </ul>
  </section>

  <section class="card card-front" aria-label="Card front">
    <div class="front-brand">
      <span class="brand-main">Stonebrook</span>
      <span class="brand-sub">Realty Partners of Chicago</span>
    </div>

    <div class="person">
      <p class="person-name">Derek Ollanby</p>
      <p class="person-title">Director of Acquisitions</p>
    </div>

    <ul class="contact">
      <li>
        <svg viewBox="0 0 20 20" aria-hidden="true"><rect x="2" y="1" width="16" height="18" rx="2"/><rect x="5" y="4" width="4" height="12" fill="#fff"/><rect x="11" y="5" width="4" height="3" fill="#fff"/><rect x="11" y="10" width="4" height="6" fill="#fff"/></svg>
        630-517-2946
      </li>
      <li>
        <svg viewBox="0 0 20 20" aria-hidden="true"><path d="M1 4h18v12H1z M3 6v8h14V6l-7 5z M4 6l6 4 6-4z" fill-rule="evenodd"/></svg>
        Derek@StonebrookRPC.com
      </li>
      <li>
        <svg viewBox="0 0 20 20" aria-hidden="true"><circle cx="10" cy="10" r="9"/><path d="M5 6c2 0 3 1 3 3s-2 2-2 4M12 3c0 3 3 3 4 5M11 17c0-3 2-3 4-4" stroke="#fff" stroke-width="1.6" fill="none"/></svg>
        www.StonebrookRPC.com
      </li>
    </ul>

    <div class="skyline-art" role="img" aria-label="Blue Chicago skyline silhouette"></div>
    <div class="front-band"></div>
  </section>

</body>
</html>
```